Breezeway Masters Business Card Design

Design new, 2 sides, business cards for a residential and light commercial heating, air conditioning contractor.

Target Market(s)

Homeowners, small businesses

Industry/Entity Type

Business

Contact Information for Business Card

Dominic Halvorsen
Phone - 862-415-2763
Email
Address - PO box 648
Succasunna NJ 07876
Website - www.BreezewayMastersLLC.example

Requirements
Must have
• logo, company colors, standard size with no die cut, so I can use nimbo press

```html
<!DOCTYPE html>
<html lang="en">
<head>
<meta charset="utf-8">
<title>Breezeway Masters Business Cards</title>
<link rel="stylesheet" href="https://fonts.googleapis.com/css2?family=Roboto:wght@400;500&family=Playfair+Display:wght@700&display=swap">
<style>
  :root {
    --backdrop: #3b312c;
    --card: #161616;
    --brand-red: #b02a3f;
    --brand-orange: #f29a2e;
    --text-light: #f1f1f1;
  }
  html, body {
    margin: 0;
    width: 1200px;
    height: 864px;
    overflow: hidden;
    background: var(--backdrop);
  }
  .stage {
    position: relative;
    width: 1200px;
    height: 864px;
  }
  .card {
    position: absolute;
    top: 278px;
    width: 540px;
    height: 309px;
    background: var(--card);
    border-radius: 3px;
    box-shadow: 0 10px 28px rgba(0,0,0,0.45);
    overflow: hidden;
  }
  .card-front { left: 40px; }
  .card-back { left: 620px; }

  .brand-name {
    font-family: "Playfair Display", Georgia, serif;
    font-weight: 700;
    color: var(--brand-orange);
    letter-spacing: 0.5px;
    display: flex;
    align-items: center;
    gap: 10px;
    white-space: nowrap;
  }
  .brand-mark {
    width: 14px;
    height: 14px;
    border-radius: 50%;
    background: var(--brand-red);
    flex: none;
  }
  .card-front .brand-name {
    position: absolute;
    left: 0; right: 0; top: 0; bottom: 0;
    justify-content: center;
    font-size: 38px;
  }
  .card-back .brand-name {
    position: absolute;
    right: 30px;
    top: 236px;
    font-size: 26px;
  }

  .contact {
    position: absolute;
    left: 34px;
    top: 32px;
    font-family: Roboto, Arial, sans-serif;
    color: var(--text-light);
  }
  .contact-name {
    margin: 0;
    font-size: 18px;
    font-weight: 500;
    color: var(--brand-red);
    letter-spacing: 0.5px;
  }
  .contact-title {
    margin: 2px 0 8px;
    font-size: 14px;
    font-weight: 500;
    color: var(--brand-orange);
    letter-spacing: 0.5px;
  }
  .contact-address {
    margin: 0 0 6px;
    font-size: 13px;
    line-height: 18px;
    font-style: normal;
  }
  .contact-list {
    list-style: none;
    margin: 0;
    padding: 0;
    font-size: 13px;
    line-height: 20px;
  }
  .contact-list li {
    display: flex;
    align-items: center;
    gap: 8px;
  }
  .contact-icon {
    width: 12px;
    height: 12px;
    fill: var(--brand-red);
    flex: none;
  }
</style>
</head>
<body>
<main class="stage">
  <section class="card card-front">
    <div class="brand-name"><span class="brand-mark"></span>Breezeway Masters</div>
  </section>

  <section class="card card-back">
    <div class="contact">
      <h1 class="contact-name">DOMINIC HALVORSEN</h1>
      <p class="contact-title">PRESIDENT</p>
      <address class="contact-address">PO box 648<br>Succasunna NJ 07876</address>
      <ul class="contact-list">
        <li>
          <svg class="contact-icon" viewBox="0 0 12 12" aria-hidden="true"><path d="M1 3c0-1 1-2 2-2l1.5 2.5-1 1c.7 1.5 1.8 2.6 3.3 3.3l1-1L10.5 8.3c0 1-1 2-2 2C4.4 10.3 1 7 1 3z"/></svg>
          862-415-2763
        </li>
        <li>
          <svg class="contact-icon" viewBox="0 0 12 12" aria-hidden="true"><path d="M3 0h6v12H3z M4 1.5v8h4v-8z"/></svg>
          862-415-2790
        </li>
        <li>
          <svg class="contact-icon" viewBox="0 0 12 12" aria-hidden="true"><path d="M3 0h5v3H3z M1 4h10v6H1z"/></svg>
          862-415-2791
        </li>
        <li>
          <svg class="contact-icon" viewBox="0 0 12 12" aria-hidden="true"><path d="M0 2h12v8H0z M1 3l5 4 5-4z" fill-rule="evenodd"/></svg>
          dominic@breezewaymasters.example
        </li>
        <li>
          <svg class="contact-icon" viewBox="0 0 12 12" aria-hidden="true"><circle cx="6" cy="6" r="5.5"/></svg>
          www.BreezewayMastersLLC.example
        </li>
      </ul>
    </div>
    <div class="brand-name"><span class="brand-mark"></span>Breezeway Masters</div>
  </section>
</main>
</body>
</html>
```